TMVB site redesign

Please redesign a home page with content provided. PSD only - no coding
Can use any images from pexorama.example

Please create a site design that more clearly illustrates the client's services and expertise. We are looking for a high-end design.

Any images used must be generic or of Dallas TX.

Fonts: Any
Colors: Match to logo
Look: Modern - Professional

Target Market(s)

medium-large business owners

Number of Pages Required

1 page

Font styles to use
Serif
Sans Serif

Requirements
Must have
• cohesive professional design
• high end look
• Match to logo

```html
<!DOCTYPE html>
<html lang="en">
<head>
<meta charset="utf-8">
<title>TMVB — Professional Office and Warehouse Leasing</title>
<link href="https://fonts.googleapis.com/css2?family=Merriweather:wght@300;400;700&family=Nunito+Sans:wght@300;400&display=swap" rel="stylesheet">
<style>
:root{
  --red:#e03a3e;
  --ink:#2b2b2b;
  --muted:#444;
  --page:#fafafa;
  --band:#f1f1f1;
  --white:#fff;
  --sky-top:#1f3366;
  --sky-mid:#2c4273;
  --city:#3a3a3f;
  --trees:#1a2016;
}
*{margin:0;padding:0;box-sizing:border-box}
html,body{width:1200px;height:1197px;overflow:hidden;background:var(--page)}
body{position:relative;font-family:"Nunito Sans",sans-serif;color:var(--ink)}
.site-header{position:absolute;left:0;top:0;width:1200px;height:94px;background:var(--white)}
.brand{position:absolute;left:114px;top:18px;width:150px;text-align:center}
.brand-name{font-family:"Merriweather",serif;font-weight:400;font-size:24px;color:var(--red);letter-spacing:1px;line-height:32px}
.brand-sub{font-family:"Merriweather",serif;font-size:8px;letter-spacing:.8px;color:var(--ink);text-transform:uppercase;margin-top:4px}
.call{position:absolute;right:141px;top:29px;font-size:15px;color:var(--ink)}
.call strong{color:var(--red);font-weight:700}
.nav a{position:absolute;top:64px;font-size:12px;color:var(--ink);text-decoration:none;text-transform:uppercase}
.nav a.active::after{content:"";position:absolute;left:0;right:0;top:26px;height:3px;background:var(--red)}
.hero{position:absolute;left:0;top:94px;width:1200px;height:598px;
  background:linear-gradient(180deg,var(--sky-top) 0%,var(--sky-mid) 40%,var(--city) 72%,var(--trees) 100%)}
.hero h1{position:absolute;left:0;width:1200px;top:176px;text-align:center;font-family:"Merriweather",serif;font-weight:400;font-size:36px;color:var(--white);text-transform:uppercase}
.hero p{position:absolute;left:0;width:1200px;top:246px;text-align:center;font-family:"Merriweather",serif;font-size:21px;line-height:24px;color:var(--white)}
.dots{position:absolute;top:562px;left:563px;display:flex;gap:6px}
.dots span{width:12px;height:12px;border-radius:50%;border:1.5px solid var(--white)}
.dots span.on{background:var(--white)}
.why h2{position:absolute;left:0;width:1200px;top:720px;text-align:center;font-family:"Merriweather",serif;font-weight:300;font-size:21px;color:var(--ink);text-transform:uppercase}
.card{position:absolute;top:772px;width:224px;height:241px;background:var(--white);box-shadow:0 1px 5px rgba(0,0,0,.18);text-align:center}
.card svg{display:block;margin:8px auto 0;width:78px;height:78px}
.card h3{font-family:"Merriweather",serif;font-weight:400;font-size:19px;margin-top:6px;color:var(--ink)}
.card p{font-size:12px;font-weight:300;line-height:16px;color:var(--muted);margin:13px auto 0;width:182px}
.cta-band{position:absolute;left:0;top:1045px;width:1200px;height:146px;background:var(--band);text-align:center}
.cta-band p{font-family:"Merriweather",serif;font-weight:300;font-size:22px;line-height:22px;margin-top:30px;color:var(--ink)}
.cta-link{display:inline-flex;align-items:center;gap:8px;margin-top:22px;font-family:"Merriweather",serif;font-weight:300;font-size:17px;color:var(--red);text-decoration:none;text-transform:uppercase}
</style>
</head>
<body>
<header class="site-header">
  <div class="brand">
    <div class="brand-name">TMVB</div>
    <div class="brand-sub">Tremont Vale Brokerage</div>
  </div>
  <div class="call">Call Today: <strong>214-555-0142</strong></div>
  <nav class="nav">
    <a class="active" href="#" style="left:516px">Services</a>
    <a href="#" style="left:627px">About TMVB</a>
    <a href="#" style="left:755px">Contact Us</a>
    <a href="#" style="left:885px">Blog</a>
    <a href="#" style="left:975px">Market News</a>
  </nav>
</header>

<section class="hero" role="img" aria-label="Dallas skyline at dusk with lit towers above a line of trees">
  <h1>Professional Office and Warehouse Leasing</h1>
  <p>Fast-track your search with tenant reps that only serve you<br>and specialize in the DFW area.</p>
  <div class="dots"><span class="on"></span><span></span><span></span></div>
</section>

<section class="why">
  <h2>Why Tenant Representation?</h2>

  <article class="card" style="left:114px">
    <svg viewBox="0 0 80 80" fill="var(--red)">
      <circle cx="17" cy="12" r="8"/><path d="M4 34a13 11 0 0 1 26 0v4H4z"/>
      <circle cx="63" cy="12" r="8"/><path d="M50 34a13 11 0 0 1 26 0v4H50z"/>
      <circle cx="40" cy="48" r="8"/><path d="M27 70a13 11 0 0 1 26 0v4H27z"/>
      <path d="M10 40q6 16 20 18M70 40q-6 16-20 18" fill="none" stroke="var(--red)" stroke-width="3"/>
    </svg>
    <h3>Relationships</h3>
    <p>Save time by trusting TMVB year after year to find the right location for you. Once we’ve worked together, we know what you need, and you can keep your budget details private.</p>
  </article>

  <article class="card" style="left:356px">
    <svg viewBox="0 0 80 80" fill="none" stroke="var(--red)" stroke-width="4">
      <path d="M14 56A34 34 0 1 0 14 24" />
      <path d="M6 28l8-8 8 8" />
      <rect x="29" y="36" width="24" height="20" rx="2"/>
      <path d="M33 36v-7a8 8 0 0 1 16 0v7"/>
    </svg>
    <h3>Access to More</h3>
    <p>We have no agreements or personal incentives for specific properties, so we can always show you the offices that are right for you.</p>
  </article>

  <article class="card" style="left:597px">
    <svg viewBox="0 0 80 80" fill="none" stroke="var(--red)" stroke-width="3">
      <circle cx="40" cy="40" r="36"/>
      <rect x="14" y="26" width="52" height="28" rx="3"/>
      <circle cx="26" cy="36" r="4"/><path d="M20 46h22M46 34h12v10H46"/>
      <path d="M14 66L66 14" stroke-width="5"/>
    </svg>
    <h3>Free To You</h3>
    <p>You pay us nothing. We get our commission from the property being leased.</p>
  </article>

  <article class="card" style="left:837px">
    <svg viewBox="0 0 80 80" fill="var(--red)">
      <circle cx="40" cy="28" r="16"/>
      <path d="M20 30v-4a20 20 0 0 1 40 0v4" fill="none" stroke="var(--red)" stroke-width="3"/>
      <rect x="16" y="26" width="7" height="12" rx="3"/><rect x="57" y="26" width="7" height="12" rx="3"/>
      <path d="M60 38q0 8-12 8" fill="none" stroke="var(--red)" stroke-width="2"/>
      <path d="M8 78a32 26 0 0 1 64 0z"/>
    </svg>
    <h3>Customized Service</h3>
    <p>Aside from saving you the time of repeating what your needs are to each new location, we also provide a report of the places you’ve seen, so it’s easier to share and make a decision.</p>
  </article>
</section>

<section class="cta-band">
  <p>If you need to find office or warehouse space in the Dallas Fort Worth area,<br>the team at TMVB has the experience you need.</p>
  <a class="cta-link" href="#">Go to Space Calculator
    <svg width="40" height="14" viewBox="0 0 40 14"><path d="M0 4h28V0l12 7-12 7v-4H0z" fill="var(--red)"/></svg>
  </a>
</section>
</body>
</html>
```